Business Card Design

Attached is my current Business card I do not like it but I must save the logo portion of it. Don't like the color or the lettering am looking for more architectural look in grays or taupe with the green more of a charturese color and the blue a charcoal color on a textured paper that looks more like something high-end that would appeal to an architect or a designer. We make concrete decorative items such as concrete fireplaces, sinks, tops and more.

Target Market(s)

Architects designers of Commercial and Residential - artistic features

Industry/Entity Type

Architect

Contact Information for Business Card

Marla T. Quinby President and Marketing Director
602-471-8836
email marla@quillstoneworks.example
Showroom "Valtique Design Center" 4128 W Larkmoor Scottsdale AZ
Fax: 602-713-4429

Font styles to use
Sans Serif

Requirements
Must have
• Architectural
Natural and earthy colors with a touch of color in the existing attached

```html
<!DOCTYPE html>
<html lang="en">
<head>
<meta charset="utf-8">
<title>Quillstone Works – Business Card</title>
<link rel="stylesheet" href="https://fonts.googleapis.com/css2?family=Jost:wght@300;400;500&display=swap">
<style>
  :root {
    --paper: #d8d1c6;
    --paper-light: #e4ded4;
    --paper-shade: #c9c1b4;
    --charcoal: #2f3235;
    --charcoal-soft: #55585b;
    --chartreuse: #a8c62b;
    --rule: rgba(47, 50, 53, 0.28);
  }
  * { margin: 0; padding: 0; box-sizing: border-box; }
  html, body {
    width: 1200px;
    height: 702px;
    overflow: hidden;
    background: var(--paper);
  }
  .card {
    position: relative;
    width: 1200px;
    height: 702px;
    overflow: hidden;
    font-family: "Jost", sans-serif;
    color: var(--charcoal);
    background:
      repeating-linear-gradient(37deg, rgba(255,255,255,0.07) 0 1px, rgba(0,0,0,0) 1px 3px),
      repeating-linear-gradient(-53deg, rgba(0,0,0,0.035) 0 1px, rgba(0,0,0,0) 1px 4px),
      radial-gradient(ellipse 900px 500px at 30% 20%, var(--paper-light), rgba(228,222,212,0) 70%),
      linear-gradient(160deg, var(--paper-light) 0%, var(--paper) 55%, var(--paper-shade) 100%);
  }
  .side-band {
    position: absolute;
    left: 0;
    top: 0;
    width: 28px;
    height: 702px;
    background: var(--charcoal);
  }
  .grid-line {
    position: absolute;
    background: var(--rule);
  }
  .grid-line--top { left: 80px; right: 80px; top: 80px; height: 1px; }
  .grid-line--bottom { left: 80px; right: 80px; bottom: 80px; height: 1px; }
  .grid-line--vertical { left: 700px; top: 380px; bottom: 80px; width: 1px; }

  .brand {
    position: absolute;
    left: 80px;
    top: 138px;
    display: flex;
    align-items: center;
    gap: 20px;
  }
  .brand-mark {
    width: 26px;
    height: 26px;
    background: var(--chartreuse);
  }
  .brand-name {
    font-size: 58px;
    line-height: 1;
    font-weight: 400;
    letter-spacing: 2px;
    color: var(--charcoal);
  }
  .accent-rule {
    position: absolute;
    left: 80px;
    top: 236px;
    width: 140px;
    height: 3px;
    background: var(--chartreuse);
  }

  .person {
    position: absolute;
    left: 80px;
    top: 282px;
  }
  .person-name {
    font-size: 38px;
    font-weight: 500;
    line-height: 1.1;
    letter-spacing: 1px;
  }
  .person-title {
    margin-top: 10px;
    font-size: 19px;
    font-weight: 300;
    letter-spacing: 4px;
    text-transform: uppercase;
    color: var(--charcoal-soft);
  }

  .contact-list {
    position: absolute;
    left: 80px;
    top: 440px;
    list-style: none;
    font-size: 24px;
    font-weight: 400;
    line-height: 46px;
  }
  .contact-label,
  .showroom-label {
    display: inline-block;
    font-size: 15px;
    font-weight: 500;
    letter-spacing: 3px;
    text-transform: uppercase;
    color: var(--charcoal-soft);
  }
  .contact-label { width: 80px; }

  .showroom {
    position: absolute;
    left: 740px;
    right: 80px;
    top: 432px;
    text-align: right;
    font-size: 24px;
    font-weight: 400;
    line-height: 40px;
  }
  .showroom-label { display: block; margin-bottom: 2px; line-height: 30px; }
  .showroom-venue { font-weight: 500; }
</style>
</head>
<body>
  <main class="card">
    <div class="side-band"></div>
    <div class="grid-line grid-line--top"></div>
    <div class="grid-line grid-line--bottom"></div>
    <div class="grid-line grid-line--vertical"></div>

    <div class="brand">
      <div class="brand-mark"></div>
      <div class="brand-name">Quillstone Works</div>
    </div>
    <div class="accent-rule"></div>

    <div class="person">
      <p class="person-name">Marla T. Quinby</p>
      <p class="person-title">President and Marketing Director</p>
    </div>

    <ul class="contact-list">
      <li><span class="contact-label">Tel</span>602-471-8836</li>
      <li><span class="contact-label">Fax</span>602-713-4429</li>
      <li><span class="contact-label">Email</span>marla@quillstoneworks.example</li>
    </ul>

    <div class="showroom">
      <span class="showroom-label">Showroom</span>
      <p class="showroom-venue">Valtique Design Center</p>
      <p>4128 W Larkmoor</p>
      <p>Scottsdale, AZ</p>
    </div>
  </main>
</body>
</html>
```